Summer orchestra weekly camp poster BVPE youth orchestra

We are youth orchestra in Texas holds a summer program called: Bright Bow Seasonal Studio (It's for students ages 8-18 who play already play violin/viola/cello/bass in the North Dallas, Texas Area.

We have 2 posters already from Artmarket designers that we have already been using and now are looking for some new designs. (you can see our other two previously purchased designs on the art market website)

The main difference in our camp is that we meet weekly on Saturday for 2 months June and July (not a week or 2 long camp like most music camps). This makes us a better choice locally because you are playing every week for 2 months out if the summer and less likely to lose skills over the summer vacation months.

Poster size: 11" by 17" but needs to be convertible to 8.5 to 11 size as well AND most importantly be in editable format via either Word or Publisher so we can use it every summer and be able to change dates, cost or location as needed.

All the details are below, but on the poster we would need the website listed: www.marlowridgeyouthensemble.example and tell them to go to that website to apply online beginning April 1st

That's how we get business, they go to our website and apply and pay with coinvault. It also needs to say really big BVPE BRIGHT BOW SEASONAL STUDIO

April 1st is when we being accepting online applications (every year, so don't put a year) Also put: Camp is held on Saturdays in June and July with final concert, last Sunday in July

Also on the poster we need: Our goal is to keep young musicians playing over the summer –so don’t put your instrument away for the summer! Keep in shape by joining us for the Marlow Ridge Youth Ensemble’s summer program – Bright Bow Seasonal Studio! Tuition is $225, which covers June/July Saturday rehearsals and the performance fee for the BKMT Hall concert, last Sunday in July.

I know we can't get all the info below on it, but I put it on so you could better understand what we are doing.

We have a logo already, that we have the rights to - I need something that kids/teens will think is cool looking and music related....we are string instruments only (violin, viola, cello, bass) we also want it to look classy looking, not cheap
I included 2 copies of the logo in different color set

here's all the details from our website:
Bright Bow Seasonal Studio (June and July) - Tuition: $225
Somewhere it should stress that we are not like other camps because we are weekly for two months. (There's a better way to state that but I'm not sure what that is)

Rehearsals on Saturdays June &July with final concert on last Sunday in July @ BKH Hall

Our goal is to keep young musicians playing over the summer –so don’t put your instrument away for the summer! Keep in shape by joining us for the Marlow Ridge Youth Ensemble’s new summer program – Bright Bow Seasonal Studio!

Tuition is $225, which covers June/July Saturday rehearsals and the performance fee for the BKMT Hall concert.

No audition is necessary. Enrollment is limited to the first 50 students in each age category, depending on instrumentation needs, so don’t delay – enrollment online begins April 1st. Siblings will receive a $50 discount, after the first child's regular priced tuition.

Bright Bow I: Students entering grades 6 and below (3:00 – 4:20 P.M. )
Bright Bow II: Students grades entering 7 and 8 (4:30 – 6:00 P.M.)
Bright Bow III: Students entering grades 9-12 (6:15 – 7:45 P.M.)

Summer camp attendance policy is more lenient due to summer vacations. Please notify BVPE of summer absences as soon as your vacation/camp dates are known.
Updates

Here is a link to the previous contest we held on ArtMarket last year.

http://jobs.artmarket.example/job.aspx?id=384619

http://poster.artmarket.example/contest.aspx?id=384619

Also Rehearsals are held at Pemberton Fiddles in Allen, TX

I am working today at a music festival and cannot get on the computer or artmarket website until after 6 or 7 p.m. tonight.  So if you are not getting feedback during the day today, that is why.  I will give feedback to everyone when I get home later tonight.  Thank you all for your work!

Reason: Hi everyone, I judged a music contest all day today and really need some time to look over all the entries. I appreciate everyone's hard work and will make a decision within the next 2 days. I want to be able to provide feedback to everyone and give everyone enough time to submit their best work, so I am extending the deadline by 2 days. I will have to make a decision at the end very quickly as we need to do a huge mail out as soon as the contest is over. Thank you everyone, we really do appreciate everyone's efforts in making our new poster for Bright Seasonal Bow Studio!

Target Market(s)

Parents of string players age 8-18 in North Texas along with students themselves.

Industry/Entity Type

Business

Requirements
Must have
• something showing we are different than the ordinary summer music camp
our QR code which I will email to you if your poster is the winner

```html
<!DOCTYPE html>
<html lang="en">
<head>
<meta charset="utf-8">
<title>BVPE Bright Bow Seasonal Studio</title>
<link rel="stylesheet" href="https://fonts.googleapis.com/css2?family=Montserrat:wght@600;700&family=Questrial&display=swap">
<style>
  :root {
    --ink: #111111;
    --night: #12141b;
    --night-deep: #07080c;
    --wood: #4a2a1a;
    --cyan: #55d6ec;
    --mint: #9fe29a;
    --lime: #c9dc4a;
    --sun: #f6b617;
    --paper: #ffffff;
  }
  * { box-sizing: border-box; margin: 0; padding: 0; }
  html, body { width: 861px; height: 1200px; overflow: hidden; background: var(--paper); }
  .poster {
    position: relative;
    width: 861px;
    height: 1200px;
    overflow: hidden;
    background: var(--paper);
    font-family: "Questrial", "Century Gothic", sans-serif;
    color: var(--ink);
  }
  .hero { position: absolute; left: 0; top: 0; width: 861px; height: 620px; }
  .hero svg { display: block; }
  .title {
    position: absolute;
    left: 34px;
    top: 40px;
    font-family: "Montserrat", "Century Gothic", sans-serif;
    font-weight: 600;
    font-size: 49px;
    line-height: 53px;
    letter-spacing: 1px;
  }
  .title span {
    display: block;
    width: max-content;
    background-clip: text;
    -webkit-background-clip: text;
    color: transparent;
  }
  .title .t1 { background-image: linear-gradient(90deg, var(--cyan), var(--mint)); }
  .title .t2 { background-image: linear-gradient(90deg, var(--cyan), var(--mint) 55%, var(--lime) 80%, var(--sun)); }
  .title .t3 { background-image: linear-gradient(90deg, var(--mint), var(--lime)); }
  .title .t4 { background-image: linear-gradient(90deg, var(--lime), var(--sun)); }
  .title .t5 { background-image: linear-gradient(90deg, var(--lime), var(--sun)); }
  .schedule {
    position: absolute;
    right: 30px;
    top: 322px;
    text-align: right;
    color: var(--paper);
    font-size: 19px;
    line-height: 23px;
  }
  .schedule strong { font-weight: 700; }
  .details {
    position: absolute;
    left: 139px;
    top: 620px;
    width: 700px;
    font-size: 15.5px;
    line-height: 19px;
  }
  .lead { color: var(--cyan); }
  .lead strong { font-weight: 700; }
  .website {
    font-family: "Montserrat", "Century Gothic", sans-serif;
    font-weight: 700;
    font-size: 22px;
    margin-top: 8px;
    color: var(--ink);
  }
  .siblings { color: var(--cyan); margin-top: 4px; }
  .siblings strong { font-weight: 700; }
  .groups { list-style: none; margin-top: 22px; }
  .groups li { line-height: 21px; }
  .groups .name { color: var(--cyan); }
  .groups .info { font-style: italic; color: var(--ink); }
  .tuition {
    margin-top: 18px;
    width: 640px;
    font-family: "Montserrat", "Century Gothic", sans-serif;
    font-weight: 700;
    font-size: 14px;
    line-height: 19px;
  }
  .goal {
    position: absolute;
    left: 139px;
    top: 936px;
    width: 700px;
    color: var(--cyan);
    font-style: italic;
    font-size: 22.5px;
    line-height: 30px;
  }
  .goal strong { font-weight: 700; }
  .brand {
    position: absolute;
    right: 60px;
    top: 1066px;
    display: flex;
    align-items: center;
    gap: 10px;
    font-family: "Montserrat", "Century Gothic", sans-serif;
    font-weight: 700;
    font-size: 30px;
    color: var(--ink);
  }
  .brand .dot { width: 22px; height: 22px; border-radius: 50%; background: var(--cyan); }
  .policy {
    position: absolute;
    left: 139px;
    top: 1132px;
    font-size: 14px;
    line-height: 19px;
    color: var(--ink);
  }
</style>
</head>
<body>
<main class="poster">
  <div class="hero">
    <svg width="861" height="620" viewBox="0 0 861 620" xmlns="http://www.w3.org/2000/svg">
      <defs>
        <linearGradient id="photoTone" x1="0" y1="0" x2="1" y2="1">
          <stop offset="0" stop-color="#1c2030"/>
          <stop offset="0.55" stop-color="#0f1016"/>
          <stop offset="0.8" stop-color="#3a2216"/>
          <stop offset="1" stop-color="#07080c"/>
        </linearGradient>
        <linearGradient id="ribbonTone" x1="0" y1="0" x2="1" y2="0">
          <stop offset="0" stop-color="#f6b617"/>
          <stop offset="0.3" stop-color="#d9d23a"/>
          <stop offset="0.5" stop-color="#9fe29a"/>
          <stop offset="0.75" stop-color="#6fe0d8"/>
          <stop offset="1" stop-color="#55e6f2"/>
        </linearGradient>
      </defs>
      <path role="img" aria-label="Photo of a musician playing the violin against a dark background"
        fill="url(#photoTone)"
        d="M0,0 H861 V395 C830,400 780,440 700,430 C620,420 560,430 470,470 C400,500 340,520 260,510 C180,500 100,530 0,555 Z"/>
      <path class="wave-ribbon" fill="url(#ribbonTone)"
        d="M0,555 C100,530 180,500 260,510 C340,520 400,500 470,470 C560,430 620,420 700,430 C780,440 830,400 861,395 L861,420 C830,432 780,470 700,460 C620,450 560,470 480,500 C400,530 340,552 260,545 C180,540 100,585 0,612 Z"/>
    </svg>
  </div>

  <h1 class="title">
    <span class="t1">BVPE</span>
    <span class="t2">BRIGHT BOW</span>
    <span class="t3">SEASONAL</span>
    <span class="t4">STUDIO</span>
  </h1>

  <p class="schedule">
    Rehearsals on Saturdays<br>
    <strong>June &amp; July</strong> with final concert<br>
    on last Sunday in July @ BKH Hall
  </p>

  <section class="details">
    <p class="lead">No audition is necessary. Enrollment is limited to the <strong>first 50 students</strong> in each age category, depending on instrumentation needs, so don't delay – enrollment online begins <strong>April 1st</strong>.</p>
    <p class="website">www.marlowridgeyouthensemble.example</p>
    <p class="siblings">Siblings will receive a <strong>$50 discount</strong>, after the first child's regular priced tuition</p>
    <ul class="groups">
      <li><span class="name">Bright Bow I:</span> <span class="info">Students entering grades 6 and below (3:00 – 4:20 P.M.)</span></li>
      <li><span class="name">Bright Bow II:</span> <span class="info">Students grades entering 7 and 8 (4:30 – 6:00 P.M.)</span></li>
      <li><span class="name">Bright Bow III:</span> <span class="info">Students entering grades 9-12 (6:15 – 7:45 P.M.)</span></li>
    </ul>
    <p class="tuition">Tuition is $225, which covers June/July Saturday rehearsals and the performance fee for the BKMT Hall concert, last Sunday in July.</p>
  </section>

  <p class="goal">
    Our goal is to keep young musicians playing over the summer –<br>
    <strong>so don't put your instrument away for the summer!</strong><br>
    Keep in shape by joining us for the Marlow Ridge Youth<br>
    Ensemble's summer program –<br>
    <strong>Bright Bow Seasonal Studio!</strong>
  </p>

  <div class="brand"><span class="dot"></span><span>BVPE</span></div>

  <p class="policy">
    Summer camp attendance policy is more lenient due to summer vacations.<br>
    Please notify BVPE of summer absences as soon as your vacation/camp dates are known.
  </p>
</main>
</body>
</html>
```